brovalo business card

We are a commercial cleaning/janitorial service company our main target is building owners and managers.
Would like to see the icon as a background shadow in the front and the full logo in white on the back with a blue background.  On the card:
Dorn Huxley, Operations Manager, dorn@brovalo.example
47315-K Pike Rd. 81 #452
Halbrook, OR 97999
555.555.0148, 800.555.0172

Updates
please include cell 555.555.0163
                                   
Thank you
If possible the fading logo on the front should be very subtle and light and lets look at centering that as well
thanks

```html
<!DOCTYPE html>
<html lang="en">
<head>
<meta charset="utf-8">
<title>brovalo business card</title>
<link rel="stylesheet" href="https://fonts.googleapis.com/css2?family=Source+Sans+3:wght@400;700&display=swap">
<style>
  :root {
    --stage: #3a3a3a;
    --navy-deep: #0f2a55;
    --navy: #1d4b8a;
    --navy-light: #4f86c2;
    --brand-blue: #1f4f99;
    --white: #ffffff;
    --paper: #f4f4f4;
    --paper-shade: #dcdcdc;
    --ink: #222222;
    --ink-soft: #444444;
  }
  * { box-sizing: border-box; margin: 0; padding: 0; }
  html, body { width: 1200px; height: 900px; overflow: hidden; }
  body {
    background: var(--stage);
    font-family: "Source Sans 3", "Myriad Pro", Arial, sans-serif;
    position: relative;
  }
  .card {
    position: absolute;
    width: 605px;
    height: 340px;
    overflow: hidden;
  }
  .card-back {
    left: 55px; top: 132px;
    background: radial-gradient(ellipse 60% 90% at 62% 30%, var(--navy-light), var(--navy) 45%, var(--navy-deep) 100%);
  }
  .card-front {
    left: 550px; top: 393px;
    background: linear-gradient(120deg, var(--paper-shade) 0%, var(--white) 45%, var(--paper) 100%);
    box-shadow: 0 4px 14px rgba(0,0,0,.35);
  }
  .backdrop-mark {
    position: absolute;
    border-radius: 50%;
  }
  .card-back .backdrop-mark {
    left: 100px; top: -10px; width: 360px; height: 360px;
    background: rgba(255,255,255,.06);
  }
  .card-front .backdrop-mark {
    left: 122px; top: -10px; width: 360px; height: 360px;
    background: rgba(0,0,0,.035);
  }
  .brand {
    position: absolute;
    display: flex;
    align-items: center;
    font-weight: 700;
    letter-spacing: -0.5px;
  }
  .brand-dot { border-radius: 50%; flex: none; }
  .card-back .brand { left: 105px; top: 118px; color: var(--white); font-size: 64px; gap: 22px; }
  .card-back .brand-dot { width: 100px; height: 100px; background: var(--white); }
  .card-front .brand { left: 323px; top: 52px; color: var(--brand-blue); font-size: 44px; gap: 14px; }
  .card-front .brand-dot { width: 60px; height: 60px; background: var(--brand-blue); }
  .web {
    position: absolute;
    left: 0; right: 0; top: 260px;
    text-align: center;
    color: var(--white);
    font-size: 21px;
  }
  .person { position: absolute; left: 137px; top: 150px; color: var(--ink); }
  .person-name { font-size: 23px; }
  .person-role { font-size: 13px; color: var(--ink-soft); margin-top: 2px; }
  .contact {
    position: absolute; left: 323px; top: 153px;
    display: grid; grid-template-columns: 59px auto;
    font-size: 18px; line-height: 24px; color: var(--ink);
  }
  .address {
    position: absolute; left: 323px; top: 268px;
    font-size: 18px; line-height: 24px; color: var(--ink);
    font-style: normal;
  }
</style>
</head>
<body>
  <section class="card card-back" aria-label="Card back">
    <div class="backdrop-mark"></div>
    <div class="brand"><span class="brand-dot"></span>brovalo</div>
    <p class="web">www.brovalo.example</p>
  </section>

  <section class="card card-front" aria-label="Card front">
    <div class="backdrop-mark"></div>
    <div class="brand"><span class="brand-dot"></span>brovalo</div>
    <div class="person">
      <p class="person-name">Dorn Huxley</p>
      <p class="person-role">Operations Manager</p>
    </div>
    <dl class="contact">
      <dt>Cell</dt><dd>555.555.0163</dd>
      <dt>Direct</dt><dd>555.555.0148</dd>
      <dt></dt><dd>800.555.0172</dd>
      <dt>Email</dt><dd>dorn@brovalo.example</dd>
    </dl>
    <address class="address">
      47315-K Pike Rd. 81 #452<br>
      Halbrook, OR 97999
    </address>
  </section>
</body>
</html>
```